Web Page for marketing online agency

We are an online marketing agency that is acing the direct response model. We engage with our customers throughout different marketing techniques as research copy-writing, advertisements and content writing. We would need a website design that will have four main aspects: The Vision; stating who we are, The Mission; stating what we do, The Team And It's Values, and a Contact Form. For this design we would want a sharp, clean and smart approach, with illustrated elements or suggestive images. You can use the attached copy, the logo, the USP and the motto. Please integrate them as you see fit while keeping in mind the previous needs and copy. This website is going to be our connection with our possible partners, future colleagues and even our clients. You may submit a design for one page or integrate the 4 different aspects on separate web pages.
Target Market(s)
business partners, future employees, age range 25-60
Industry/Entity Type
Direct Marketing
Number of Pages Required
1 page
Requirements
Must have
- Menu / Header
- 4 Parts or 4 Pages including: vision, mission, team, contact
- Logo
- Motto: Direct Brilliance
- USP: We help people help themselves.
- The copy attached
Nice to have
- Representative illustrated images or elements
Should not have
- A boring design, classical design - Pagequill like

```html
<!DOCTYPE html>
<html lang="en">
<head>
<meta charset="utf-8">
<title>Novaline — Direct Brilliance</title>
<link href="https://fonts.googleapis.com/css2?family=Montserrat:wght@600;700;800&family=Open+Sans:wght@400;600;700&display=swap" rel="stylesheet">
<style>
:root{
  --teal:#1fb7c9;
  --teal-deep:#0f8ea6;
  --teal-light:#5fd8e0;
  --aqua:#8ff0ee;
  --navy:#0d5f78;
  --footer:#0e6f86;
  --footer-dark:#0a5a6e;
  --ink:#2b3a42;
  --muted:#8a969c;
  --white:#ffffff;
  --accent:#f06b2a;
}
*{box-sizing:border-box;margin:0;padding:0}
html,body{width:1200px;height:2736px;overflow:hidden}
body{position:relative;background:var(--white);font-family:"Open Sans",Arial,sans-serif;color:var(--ink)}
.abs{position:absolute}
h2,h3,.brand,.hero-title{font-family:"Montserrat","Open Sans",sans-serif}

/* hero */
.hero{left:0;top:0;width:1200px;height:900px}
.hero-bg{position:absolute;inset:0}
.brand{left:42px;top:16px;display:flex;align-items:center;gap:8px;color:var(--white);font-size:30px;font-weight:700}
.brand-dot{width:14px;height:14px;border-radius:50%;background:var(--white)}
.nav{left:600px;top:40px;display:flex;align-items:center;gap:40px;font-size:13px;font-weight:600;color:var(--white)}
.nav .quote{border:1.5px solid var(--white);border-radius:3px;padding:6px 16px}
.hero-title{left:0;width:1200px;top:100px;text-align:center;color:var(--white);font-size:46px;font-weight:800}
.hero-sub{left:0;width:1200px;top:168px;text-align:center;color:var(--white);font-size:17px;font-weight:600}
.hero-art{left:380px;top:220px;width:440px;height:380px;border-radius:50%;background:radial-gradient(circle,#ffffff 0%,#e9fbfc 45%,rgba(255,255,255,0) 72%)}

/* sections */
.section-title{left:0;width:1200px;text-align:center;font-size:24px;font-weight:700;color:var(--ink)}
.section-kicker{left:0;width:1200px;text-align:center;font-size:12px;color:var(--muted)}
.lead{left:250px;width:700px;text-align:center;font-size:12px;line-height:1.7;color:var(--muted)}

.values{left:230px;top:1115px;width:740px;display:flex;justify-content:space-between}
.value{width:170px;text-align:center}
.value-icon{width:62px;height:62px;margin:0 auto 14px;display:block}
.value h3{font-size:12px;font-weight:700;letter-spacing:.5px;color:var(--ink);margin-bottom:8px}
.value p{font-size:11px;line-height:1.6;color:var(--muted)}

.mission{left:240px;top:1385px;width:340px}
.mission h2{font-size:24px;font-weight:700;color:var(--ink);text-align:right}
.mission .kicker{font-size:12px;color:var(--muted);text-align:right;margin:4px 0 26px}
.mission p{font-size:12px;line-height:1.75;color:var(--muted)}
.btn{display:inline-block;margin:26px 0 0 130px;background:var(--teal);color:var(--white);font-size:12px;font-weight:600;padding:10px 22px;border-radius:3px}
.mission-art{left:610px;top:1310px;width:370px;height:440px}

.cards{left:225px;top:1920px;width:750px;display:flex;gap:30px}
.card{flex:1;height:140px;background:var(--white);border-radius:4px;box-shadow:0 6px 22px rgba(15,80,100,.14);display:flex;gap:18px;padding:26px 24px}
.avatar{flex:none;width:62px;height:62px;border-radius:50%;background:linear-gradient(135deg,#c9b8a8,#6f6259)}
.card h3{font-size:11px;font-weight:700;color:var(--teal);margin-bottom:8px}
.card p{font-size:11px;line-height:1.6;color:var(--muted)}

/* footer */
.waves{left:0;top:2060px;width:1200px;height:330px}
.footer{left:0;top:2330px;width:1200px;height:406px;background:var(--footer)}
.fcol{color:var(--white);font-size:11px}
.fcol h4{font-family:"Montserrat",sans-serif;font-size:13px;font-weight:700;margin-bottom:6px}
.rule{width:36px;height:2px;background:var(--teal-light);margin-bottom:14px}
.about{left:230px;top:2390px;width:270px}
.about p{line-height:1.7;color:#cfeef2}
.social{display:flex;gap:6px;margin-top:18px}
.social span{width:22px;height:22px;border:1px solid #9fdde6;border-radius:2px}
.links{left:582px;top:2390px;width:150px}
.links li{list-style:none;line-height:2.1;color:#cfeef2}
.links li::before{content:"›";margin-right:8px;color:var(--teal-light)}
.contact{left:775px;top:2390px;width:200px}
.field{height:22px;background:rgba(255,255,255,.12);border:1px solid rgba(255,255,255,.25);margin-bottom:6px;color:#cfeef2;font-size:10px;padding:4px 8px}
.field.msg{height:38px}
.send{display:inline-block;background:var(--teal);color:var(--white);font-size:10px;font-weight:600;padding:5px 14px;border-radius:2px}
.bar{left:225px;top:2630px;width:750px;height:42px;border-radius:3px;background:var(--footer-dark);display:flex;align-items:center;justify-content:space-around;color:#cfeef2;font-size:10px}
.bar span{display:flex;align-items:center;gap:6px}
.copy{left:0;top:2704px;width:1200px;text-align:center;color:#a9dbe3;font-size:10px}
</style>
</head>
<body>

<section class="hero abs">
  <svg class="hero-bg" width="1200" height="900" viewBox="0 0 1200 900" preserveAspectRatio="none">
    <defs>
      <linearGradient id="heroGrad" x1="0" y1="0" x2="0" y2="1">
        <stop offset="0" stop-color="#1aa9c6"/>
        <stop offset="1" stop-color="#2fd0d6"/>
      </linearGradient>
    </defs>
    <path d="M0 0H1200V770C1050 720 900 800 720 790C560 780 460 820 300 800C180 785 80 760 0 790Z" fill="url(#heroGrad)"/>
    <path d="M0 790C90 760 190 790 320 812C470 836 600 790 760 805C920 820 1050 760 1200 790V830C1060 800 930 850 760 845C600 840 460 870 300 850C170 834 80 810 0 830Z" fill="#8ff0ee" opacity=".7"/>
  </svg>
  <div class="brand abs"><span>Novaline</span><span class="brand-dot"></span></div>
  <nav class="nav abs"><span>Home</span><span>Mission</span><span>Team</span><span>Contact</span><span class="quote">Quotes</span></nav>
  <h1 class="hero-title abs">We Help People Help Themselves.</h1>
  <p class="hero-sub abs">We are specialized in the self-reliance mindset &amp; to grow individually</p>
  <div class="hero-art abs" role="img" aria-label="Illustration of a megaphone with a cloud, target, video and marketing icons"></div>
</section>

<h2 class="section-title abs" style="top:990px">Who we are ?</h2>
<p class="section-kicker abs" style="top:1024px">Our Vision</p>
<p class="lead abs" style="top:1050px">We are a direct response company that builds real trust with people and partners. Our approach mixes research, copy and creative campaigns that help every individual grow with confidence and direction.</p>

<div class="values abs">
  <div class="value">
    <svg class="value-icon" viewBox="0 0 62 62"><circle cx="31" cy="31" r="30" fill="#e3f8fa"/><path d="M31 14L44 22V30C44 38 38 45 31 48C24 45 18 38 18 30V22Z" fill="var(--teal)"/></svg>
    <h3>HONOR</h3><p>We deliver honest work through every phase, keeping each promise clear, simple, fair and direct.</p>
  </div>
  <div class="value">
    <svg class="value-icon" viewBox="0 0 62 62"><circle cx="31" cy="31" r="30" fill="#e3f8fa"/><path d="M31 46L17 32C13 27 16 19 23 19C27 19 29 22 31 24C33 22 35 19 39 19C46 19 49 27 45 32Z" fill="var(--teal)"/></svg>
    <h3>CARING</h3><p>We listen closely to clients and colleagues, giving time, support and attention to real needs.</p>
  </div>
  <div class="value">
    <svg class="value-icon" viewBox="0 0 62 62"><circle cx="31" cy="31" r="30" fill="#e3f8fa"/><rect x="20" y="28" width="22" height="18" rx="2" fill="var(--teal)"/><path d="M24 28V23A7 7 0 0 1 38 23V28" fill="none" stroke="var(--teal)" stroke-width="3"/></svg>
    <h3>SAFETY</h3><p>We protect the data and trust of partners, keeping every project secure, stable and well guided.</p>
  </div>
  <div class="value">
    <svg class="value-icon" viewBox="0 0 62 62"><circle cx="31" cy="31" r="30" fill="#e3f8fa"/><path d="M16 36L31 18L46 36L38 33L31 44L24 33Z" fill="var(--teal)"/></svg>
    <h3>FREEDOM</h3><p>We give people room to think, create and decide, so every idea has space to grow freely.</p>
  </div>
</div>

<div class="mission abs">
  <h2>What is it that we do?</h2>
  <p class="kicker">Our Mission</p>
  <p>We help individuals and teams find the right message and reach the right audience. Through research, copywriting, advertising and content writing we build campaigns that speak directly to people, invite a clear response and turn attention into lasting results for every client and partner we work with.</p>
  <span class="btn">Learn more</span>
</div>
<div class="mission-art abs" role="img" aria-label="Illustration of a person working at a desk with a laptop and office items inside a teal blob shape">
  <svg width="370" height="440" viewBox="0 0 370 440">
    <defs><linearGradient id="blobGrad" x1="0" y1="0" x2="1" y2="1"><stop offset="0" stop-color="#2fc3d4"/><stop offset="1" stop-color="#138fa8"/></linearGradient></defs>
    <path d="M185 20C290 10 360 90 350 200C345 300 290 420 180 425C80 430 15 340 20 230C25 140 70 30 185 20Z" fill="url(#blobGrad)"/>
    <circle cx="190" cy="215" r="130" fill="#e9fbfc" opacity=".85"/>
  </svg>
</div>

<h2 class="section-title abs" style="top:1772px">Our Team</h2>
<p class="section-kicker abs" style="top:1806px">Values</p>
<p class="lead abs" style="top:1832px">We are a small team that likes to move fast and think clearly. Every member brings energy, care and practical skills to each campaign we build together.</p>

<div class="cards abs">
  <div class="card">
    <div class="avatar" role="img" aria-label="Portrait photo of team member"></div>
    <div><h3>DANIEL MARSH - TEAM LEADERSHIP</h3><p>Guides the team with calm focus, shaping strategy, setting goals and keeping every campaign on track from start to final result.</p></div>
  </div>
  <div class="card">
    <div class="avatar" role="img" aria-label="Portrait photo of team member"></div>
    <div><h3>LENA CORBIN - COPYWRITER</h3><p>Writes sharp, honest copy that speaks to real people and invites them to respond, act and stay connected.</p></div>
  </div>
</div>

<svg class="waves abs" width="1200" height="330" viewBox="0 0 1200 330" preserveAspectRatio="none">
  <path d="M0 120C150 60 300 110 470 140C650 170 820 60 1000 70C1090 75 1150 100 1200 90V330H0Z" fill="#8ff0ee"/>
  <path d="M0 170C180 120 330 200 520 190C700 180 860 110 1040 130C1110 138 1160 150 1200 140V330H0Z" fill="#3fcfd8"/>
  <path d="M0 230C200 190 380 250 580 240C770 230 940 190 1200 210V330H0Z" fill="#1aa6bf"/>
  <path d="M0 260C220 240 420 280 620 275C820 270 1000 250 1200 262V330H0Z" fill="#0e6f86"/>
</svg>

<footer class="footer abs"></footer>
<div class="fcol about abs">
  <h4>About Company</h4><div class="rule"></div>
  <p>We are a direct response marketing team that helps people help themselves. Our work blends research, copy and content to build campaigns that are clear, honest and made to last.</p>
  <div class="social"><span></span><span></span><span></span><span></span><span></span></div>
</div>
<div class="fcol links abs">
  <h4>Quick Links</h4><div class="rule"></div>
  <ul><li>Home</li><li>Mission</li><li>Vision</li><li>Team</li><li>Contact</li><li>Quotes</li></ul>
</div>
<div class="fcol contact abs">
  <h4>Contact Us</h4><div class="rule"></div>
  <div class="field">Name</div>
  <div class="field">Email</div>
  <div class="field">Phone</div>
  <div class="field msg">Message</div>
  <span class="send">Submit</span>
</div>

<div class="bar abs">
  <span><svg width="12" height="12" viewBox="0 0 12 12"><path d="M2 1L4 1L5 4L3.5 5C4.3 6.7 5.3 7.7 7 8.5L8 7L11 8V10C11 10.6 10.6 11 10 11C5 11 1 7 1 2C1 1.4 1.4 1 2 1Z" fill="#5fd8e0"/></svg>Tel: +1 555 0142 880</span>
  <span><svg width="13" height="10" viewBox="0 0 13 10"><rect x=".5" y=".5" width="12" height="9" fill="none" stroke="#5fd8e0"/><path d="M.5 .5L6.5 5.5L12.5 .5" fill="none" stroke="#5fd8e0"/></svg>hello@novaline.example</span>
  <span><svg width="10" height="13" viewBox="0 0 10 13"><path d="M5 12C5 12 1 7.5 1 5A4 4 0 0 1 9 5C9 7.5 5 12 5 12Z" fill="#5fd8e0"/><circle cx="5" cy="5" r="1.5" fill="#0a5a6e"/></svg>21 Harbor Lane, Suite 4, Westbridge</span>
</div>
<p class="copy abs">© Copyright 2024 Novaline. All rights reserved.</p>

</body>
</html>
```